Fully Functional Wix Website, Not Just Images

Please read all instructions carefully. This is NOT merely a design project where the artist will deliver static images. This project requires that the designer build a fully functional SEO optimized website within Wix then transfer full ownership to me. See attached "instructions for design" file. I have wix for other websites. Only wix is acceptable. Do not submit more than 1 design per designer. If you submit more than 1 design I will award to someone else.

Target Market(s)

see attachments and trelvanox482.com

Industry/Entity Type

Coding

Coded - Design and coding required

Number of Pages Required

4 page

Font styles to use
Other font styles liked:
• see attachments and trelvanox482.com

Requirements
Must have
Nice to have
Should not have

```html
<!DOCTYPE html>
<html lang="en">
<head>
<meta charset="utf-8">
<title>Captain Harlan's Boat Training &amp; Charters</title>
<link href="https://fonts.googleapis.com/css2?family=Cinzel:wght@400;500;600;700&family=EB+Garamond:ital,wght@0,400;0,500;0,600;1,400&display=swap" rel="stylesheet">
<style>
:root{
  --navy:#1c3352;
  --navy-dark:#14263f;
  --gold:#c9a253;
  --tan:#c7a06a;
  --ink:#1b1b1b;
  --muted:#555;
  --soft:#f3f3f3;
  --line:#e2e2e2;
  --white:#fff;
}
*{box-sizing:border-box;margin:0;padding:0}
html,body{width:1200px;height:4087px;overflow:hidden}
body{background:var(--white);font-family:"EB Garamond",Georgia,serif;color:var(--ink);position:relative}
.wrap{width:1012px;margin:0 auto;position:relative}
.display{font-family:"Cinzel",Georgia,serif;font-weight:600;letter-spacing:.5px}
.eyebrow{font-size:11px;letter-spacing:2px;color:var(--gold);text-transform:uppercase}
.anchor-ico{width:16px;height:16px;display:block}
.btn{display:inline-flex;align-items:center;gap:10px;font-size:13px;padding:0 14px;height:36px;border-radius:2px}
.btn-tan{background:var(--tan);color:var(--ink)}
.btn-outline{border:1.5px solid var(--ink);background:var(--white)}
.btn-dark{background:#111;color:#fff}
.ring{width:18px;height:18px;border-radius:50%;border:1.5px solid currentColor;display:inline-flex;align-items:center;justify-content:center;font-size:10px}
.ph{display:block}

/* header */
.site-header{height:102px;background:#f6f6f6;position:relative}
.brand{position:absolute;left:94px;top:14px;display:flex;align-items:center;gap:14px}
.brand-mark{width:74px;height:74px;border-radius:50%;background:var(--navy);border:3px solid var(--gold)}
.brand-name{font-size:12.5px;line-height:1.4;text-transform:uppercase;letter-spacing:.3px}
.main-nav{position:absolute;left:454px;top:42px;display:flex;gap:18px;font-size:12.5px}
.main-nav a{padding:2px 7px}
.main-nav .active{background:#eadfcb}
.header-actions{position:absolute;right:94px;top:34px;display:flex;align-items:center;gap:18px;font-size:12px}
.header-actions .btn{height:30px;font-size:11px}

/* hero */
.hero{height:557px;position:relative;background:linear-gradient(90deg,#e8ebef 0%,#d5dbe3 45%,#9aa6b4 100%)}
.hero-photo{position:absolute;inset:0}
.hero-copy{position:absolute;left:94px;top:228px;width:400px}
.hero-copy .eyebrow{color:#333;display:flex;gap:10px;align-items:center;font-size:10.5px}
.hero-title{font-size:50px;line-height:1.15;margin-top:10px;color:#111}
.hero-tags{display:inline-block;background:#fff;font-size:11px;letter-spacing:1.6px;padding:4px 16px;margin-top:12px;text-transform:uppercase}
.hero-text{font-size:13px;line-height:1.35;margin-top:14px;width:380px}
.hero-btns{display:flex;gap:8px;margin-top:28px}
.badges{position:absolute;right:94px;bottom:30px;display:flex;gap:14px}
.badge{width:70px;height:70px;border-radius:50%;background:#fff;border:3px dotted var(--gold)}
.badge i{display:block;margin:10px;width:44px;height:44px;border-radius:50%;background:var(--navy)}

/* series */
.series{padding-top:87px;height:722px}
.section-head{position:relative}
.section-head h2{font-size:34px;margin-top:6px}
.section-head .btn{position:absolute;right:0;bottom:0;height:38px;font-size:12px}
.books{display:flex;gap:12px;margin-top:36px}
.book{width:329px}
.book-cover{height:338px;background:var(--navy);position:relative}
.book-cover .ph{position:absolute;left:76px;top:50px;width:178px;height:240px;background:linear-gradient(160deg,#2c4d7a,#c9a253 60%,#1c3352)}
.book-cover svg.arrow{position:absolute;right:14px;bottom:16px}
.book-title{text-align:center;font-size:13.5px;margin-top:14px;text-transform:uppercase;letter-spacing:.4px;font-weight:500}

/* about */
.meet{text-align:center;height:132px}
.meet .anchor-ico{margin:0 auto}
.meet .eyebrow{margin-top:8px}
.meet h2{font-size:34px;margin-top:8px}
.about{height:462px;background:var(--soft);position:relative;margin-top:1px}
.about-photo{position:absolute;left:0;top:0;width:515px;height:462px;background:radial-gradient(circle at 60% 40%,#dadde2,#bfc4cc)}
.about-frame{position:absolute;left:515px;top:60px;width:10px;height:340px;border:1px solid var(--gold);border-left:none}
.about-copy{position:absolute;left:592px;top:80px;width:506px}
.about-copy h3{font-weight:400;font-size:30px;line-height:1.2}
.about-copy p{font-size:12.5px;line-height:1.55;color:#333;margin-top:18px}
.about-copy .btn{margin-top:22px;height:38px;font-size:12px}
.about-copy blockquote{margin-top:42px;font-size:15px}
.about-copy cite{display:block;font-size:12px;font-weight:600}

.creds{height:254px;position:relative;background:linear-gradient(#fff 0,#fff 70%,#f3f3f3 100%)}
.creds ul{list-style:none;display:flex;justify-content:space-between;width:1012px;margin:0 auto;padding-top:52px}
.creds li{width:190px;text-align:center;font-size:12px;line-height:1.5}
.cred-ico{width:80px;height:80px;border-radius:50%;border:3px dotted var(--gold);margin:0 auto 12px;display:flex;align-items:center;justify-content:center}

/* reviews */
.reviews{height:633px;background:#f3f3f3;position:relative;overflow:hidden;text-align:center;padding-top:94px}
.reviews .anchor-ico{margin:0 auto}
.reviews .eyebrow{margin-top:8px}
.reviews h2{font-size:32px;margin-top:8px}
.reviews .sub{font-size:11.5px}
.reviews .stars{color:var(--gold);letter-spacing:1px}
.review{position:absolute;width:294px;height:154px;background:#fff;border:1px solid var(--line);text-align:left;padding:22px 20px}
.review .src{position:absolute;right:18px;top:12px;font-size:15px;color:#6a7fa8}
.review .who{display:flex;gap:10px;align-items:center}
.review .av{width:26px;height:26px;border-radius:50%;background:#8a97ab;flex:none}
.review .nm{font-size:11.5px;font-weight:600}
.review .nm small{display:block;font-weight:400;color:#888;font-size:10px}
.review p{font-size:11.5px;line-height:1.5;color:#333;margin-top:14px}
.fade-l,.fade-r{position:absolute;top:210px;width:260px;height:340px}
.fade-l{left:0;background:linear-gradient(90deg,#f3f3f3 20%,rgba(243,243,243,0))}
.fade-r{right:0;background:linear-gradient(270deg,#f3f3f3 20%,rgba(243,243,243,0))}

/* services */
.services{padding-top:80px;height:587px}
.svc-row{display:flex;gap:13px;margin-top:30px}
.svc{width:243px;height:302px;background:var(--navy);color:#fff;position:relative;padding:8px}
.svc .ph{height:180px;background:linear-gradient(180deg,#9db4cc,#4a6480)}
.svc-ico{position:absolute;left:26px;top:150px;width:48px;height:48px;border-radius:50%;background:#fff;display:flex;align-items:center;justify-content:center;color:var(--navy)}
.svc h4{font-family:"Cinzel",serif;font-weight:600;font-size:13.5px;margin:34px 0 0 18px;letter-spacing:.5px}
.svc p{font-size:11px;line-height:1.45;margin:6px 0 0 18px;color:#d9dfe8;width:150px}
.svc .go{position:absolute;right:22px;bottom:24px}
.svc-feature .ph{height:250px;background:linear-gradient(180deg,#a9bfd4 0%,#6f87a2 55%,#2a4260 100%)}
.svc-feature h4{position:absolute;left:26px;top:192px;margin:0}
.svc-feature p{position:absolute;left:26px;top:214px;margin:0;width:180px}
.svc-feature .link{position:absolute;left:26px;bottom:20px;font-size:11px;color:#d9c08c;border-top:1px solid #5a6f8c;width:190px;padding-top:6px}
.svc-feature .go{bottom:22px}

/* contact */
.contact{width:1012px;margin:0 auto;height:397px;display:flex}
.contact-form{width:554px;background:var(--soft);padding:50px 76px 0}
.contact-form h2{font-size:34px;line-height:1.25}
.fields{display:grid;grid-template-columns:1fr 1fr;gap:8px 12px;margin-top:16px}
.field{background:#fff;height:36px;font-size:11px;color:#888;padding:10px 12px}
.field.wide{grid-column:1/3;height:48px}
.submit{margin-top:14px;height:38px;border:1.5px solid #222;background:#fff;display:flex;align-items:center;justify-content:center;font-size:11.5px}
.contact-photo{flex:1;background:linear-gradient(160deg,#7ea3c6,#2f5e8e 60%,#1d3f66)}

/* footer */
.site-footer{position:absolute;left:0;top:3849px;width:1200px}
.foot-brand{position:absolute;left:94px;top:0;width:240px}
.foot-brand .brand-mark{width:70px;height:70px}
.foot-brand h5{font-size:12px;font-weight:500;margin-top:22px}
.foot-brand p{font-size:11px;line-height:1.5;color:#444;margin-top:4px}
.foot-divider{position:absolute;left:405px;top:0;width:1px;height:150px;background:var(--line)}
.foot-col{position:absolute;top:24px;font-size:11px;line-height:1.9;color:#555}
.foot-col h6{font-size:11.5px;font-weight:600;color:#222;margin-bottom:10px}
.foot-col li{list-style:none;display:flex;gap:10px;align-items:center}
.foot-col .mail{color:var(--gold);text-decoration:underline}
.copyright{position:absolute;top:4045px;left:0;width:1200px;border-top:1px solid var(--line);padding-top:12px;text-align:center;font-size:10.5px;color:#444}
</style>
</head>
<body>

<header class="site-header">
  <div class="brand">
    <div class="brand-mark"></div>
    <div class="brand-name">Captain Harlan's Boat<br>Training &amp; Charters, LLC</div>
  </div>
  <nav class="main-nav">
    <a class="active">Home</a><a>Services</a><a>Boating Aids</a><a>Gallery</a><a>Contact</a>
  </nav>
  <div class="header-actions">
    <span>&#8677; Log In</span>
    <span class="btn btn-dark">Get in Touch <span class="ring">&#8595;</span></span>
  </div>
</header>

<section class="hero">
  <div class="hero-photo" role="img" aria-label="Photograph of two smiling captains at the helm of a white boat on the bay"></div>
  <div class="hero-copy">
    <div class="eyebrow">
      <svg class="anchor-ico" viewBox="0 0 16 16" fill="none" stroke="#222" stroke-width="1.4"><circle cx="8" cy="3" r="1.6"/><path d="M8 4.6V14M4.5 7h7M2.5 10a5.5 5 0 0 0 11 0"/></svg>
      Know before you go
    </div>
    <h1 class="hero-title display">CONFIDENCE<br>AT THE HELM</h1>
    <div class="hero-tags">Training &nbsp;•&nbsp; Charters &nbsp;•&nbsp; Real-world knowledge</div>
    <p class="hero-text">Whether you're new to boating or ready for your next adventure, Captain Harlan's Boat Training &amp; Charters, LLC helps you build skills, make memories, and explore with confidence.</p>
    <div class="hero-btns">
      <span class="btn btn-tan">Explore our charters <span class="ring">&#8595;</span></span>
      <span class="btn btn-outline">View Boat Training <span class="ring">&#8595;</span></span>
    </div>
  </div>
  <div class="badges">
    <div class="badge"><i></i></div><div class="badge"><i></i></div><div class="badge"><i></i></div>
  </div>
</section>

<section class="series">
  <div class="wrap">
    <div class="section-head">
      <svg class="anchor-ico" viewBox="0 0 16 16" fill="none" stroke="#222" stroke-width="1.4"><circle cx="8" cy="3" r="1.6"/><path d="M8 4.6V14M4.5 7h7M2.5 10a5.5 5 0 0 0 11 0"/></svg>
      <div class="eyebrow" style="margin-top:8px">Knowledge for a better boating tomorrow</div>
      <h2 class="display">THE FIRST MATE SERIES</h2>
      <span class="btn btn-tan">View the First Mate Series <span class="ring">&#8595;</span></span>
    </div>
    <div class="books">
      <div class="book">
        <div class="book-cover">
          <div class="ph" role="img" aria-label="Book cover of First Mate Buy showing a bridge at sunset"></div>
          <svg class="arrow" width="28" height="10" viewBox="0 0 28 10" fill="none" stroke="#c9a253"><path d="M0 5h26M22 1l4 4-4 4"/></svg>
        </div>
        <div class="book-title">First Mate Buy</div>
      </div>
      <div class="book">
        <div class="book-cover">
          <div class="ph" role="img" aria-label="Book cover of First Mate Trip showing a motorboat on the water"></div>
          <svg class="arrow" width="28" height="10" viewBox="0 0 28 10" fill="none" stroke="#c9a253"><path d="M0 5h26M22 1l4 4-4 4"/></svg>
        </div>
        <div class="book-title">First Mate Trip</div>
      </div>
      <div class="book">
        <div class="book-cover">
          <div class="ph" role="img" aria-label="Book cover of First Mate Throttle showing a boat before a city skyline"></div>
          <svg class="arrow" width="28" height="10" viewBox="0 0 28 10" fill="none" stroke="#c9a253"><path d="M0 5h26M22 1l4 4-4 4"/></svg>
        </div>
        <div class="book-title">First Mate Throttle</div>
      </div>
    </div>
  </div>
</section>

<section class="meet">
  <svg class="anchor-ico" viewBox="0 0 16 16" fill="none" stroke="#222" stroke-width="1.4"><circle cx="8" cy="3" r="1.6"/><path d="M8 4.6V14M4.5 7h7M2.5 10a5.5 5 0 0 0 11 0"/></svg>
  <div class="eyebrow">Meet Captain Harlan</div>
  <h2 class="display">EDUCATED &amp; PROFESSIONAL</h2>
</section>

<section class="about">
  <div class="about-photo" role="img" aria-label="Portrait photograph of the captain in a grey uniform shirt"></div>
  <div class="about-frame"></div>
  <div class="about-copy">
    <h3>Experience. Knowledge.<br>A safer tomorrow.</h3>
    <p>I'm Captain Harlan — a licensed captain, certified boating instructor, and author of the First Mate series. With years of hands-on experience on the water, I'm passionate about helping others build the skills and confidence to boat safely and enjoyably. Whether you're training, chartering, or just looking for trusted guidance, I'm here to help you make the most of your time on the water.</p>
    <span class="btn btn-outline">More About Captain Harlan <span class="ring">&#8595;</span></span>
    <blockquote>“Good boaters make brighter tomorrows.”<cite><i>– Captain Harlan</i></cite></blockquote>
  </div>
</section>

<section class="creds">
  <ul>
    <li><div class="cred-ico"><svg width="34" height="34" viewBox="0 0 24 24" fill="none" stroke="#1c3352" stroke-width="1.3"><rect x="3" y="4" width="16" height="13" rx="1"/><path d="M6 8h10M6 11h7"/><circle cx="17" cy="17" r="3"/></svg></div>National Marine Authority Licensed<br>Captain (Master, Near Coastal)</li>
    <li><div class="cred-ico"><svg width="34" height="34" viewBox="0 0 24 24" fill="none" stroke="#1c3352" stroke-width="1.3"><circle cx="12" cy="7" r="3"/><path d="M6 20c0-4 3-7 6-7s6 3 6 7"/></svg></div>Committed to safer,<br>more confident boaters</li>
    <li><div class="cred-ico"><svg width="34" height="34" viewBox="0 0 24 24" fill="none" stroke="#1c3352" stroke-width="1.3"><path d="M4 6l8-3 8 3-8 3z M4 10l8 3 8-3M4 14l8 3 8-3"/></svg></div>Published author —<br>the First Mate series</li>
    <li><div class="cred-ico"><svg width="34" height="34" viewBox="0 0 24 24" fill="none" stroke="#1c3352" stroke-width="1.3"><circle cx="12" cy="9" r="5"/><path d="M9 13l-2 8 5-3 5 3-2-8"/></svg></div>Years of real-world<br>charter experience</li>
    <li><div class="cred-ico"><svg width="34" height="34" viewBox="0 0 24 24" fill="none" stroke="#1c3352" stroke-width="1.3"><circle cx="12" cy="7" r="3.5"/><path d="M5 21v-3c0-3 3-5 7-5s7 2 7 5v3z"/></svg></div>Certified boating<br>instructor</li>
  </ul>
</section>

<section class="reviews">
  <svg class="anchor-ico" viewBox="0 0 16 16" fill="none" stroke="#222" stroke-width="1.4"><circle cx="8" cy="3" r="1.6"/><path d="M8 4.6V14M4.5 7h7M2.5 10a5.5 5 0 0 0 11 0"/></svg>
  <div class="eyebrow">Real boaters. Real experiences.</div>
  <h2 class="display">RATEWELL REVIEWS</h2>
  <div class="sub">See what our students and charter guests are saying. <span class="stars">★★★★★</span></div>

  <div class="review" style="left:-207px;top:221px"><span class="src">Ratewell</span><p style="margin-top:60px">Great trip, highly recommend it to everyone!</p></div>
  <div class="review" style="left:100px;top:221px"><span class="src">Ratewell</span><div class="who"><span class="av"></span><span class="nm">Dale Morrow<small>4 days ago</small></span></div><p>Really good training. I would recommend Capt. Harlan to any new boat owner!</p></div>
  <div class="review" style="left:408px;top:221px"><span class="src">Ratewell</span><div class="who"><span class="av"></span><span class="nm">Kinsey Albright<small>1 month ago</small></span></div><p>Captain Harlan doesn't only have a cool name. He is amazing at what he does. His level of patience, knowledge, and teaching abilities is top notch.</p></div>
  <div class="review" style="left:716px;top:221px"><span class="src">Ratewell</span><div class="who"><span class="av"></span><span class="nm">Oscar Lindqvist<small>3 months ago</small></span></div><p>Lots of useful information that will help me to stay safe and enjoy my time in the water. Very patient and well structured method to teach. Highly recommended!!</p></div>
  <div class="review" style="left:1024px;top:221px"><span class="src">Ratewell</span><div class="who"><span class="av"></span><span class="nm">Peter Vance<small>1 month ago</small></span></div><p>Captain Harlan was safe, calm and all around nice guy. Can't wait.</p></div>

  <div class="review" style="left:-8px;top:388px"><span class="src">Ratewell</span><div class="who"><span class="av"></span><span class="nm">Marla Keene<small>1 month ago</small></span></div><p>Captain Harlan was very knowledgeable and kept us having fun. We had a wonderful time on the water. I highly recommend him!!!</p></div>
  <div class="review" style="left:298px;top:388px"><span class="src">Ratewell</span><div class="who"><span class="av"></span><span class="nm">Nadia Corral<small>1 month ago</small></span></div><p>He's a great teacher—very friendly, patient, and knowledgeable. He made learning easy and enjoyable, and I felt comfortable throughout the entire lesson. I highly recommend him!</p></div>
  <div class="review" style="left:605px;top:388px"><span class="src">Ratewell</span><div class="who"><span class="av"></span><span class="nm">Tessa Moreau<small>2 months ago</small></span></div><p>Got to learn a lot just from one lesson with Captain Harlan. Definitely recommend if you are wanting to get into the boat life in FL.</p></div>
  <div class="review" style="left:913px;top:388px"><span class="src">Ratewell</span><div class="who"><span class="av"></span><span class="nm">Walter Greer<small>2 months ago</small></span></div><p>Extremely knowledgeable. Technical, great attention to detail, very patient, demonstrates actions and lets you practice, safety conscience and shows passion for teaching.</p></div>
  <div class="fade-l"></div><div class="fade-r"></div>
</section>

<section class="services">
  <div class="wrap">
    <div class="section-head">
      <svg class="anchor-ico" viewBox="0 0 16 16" fill="none" stroke="#222" stroke-width="1.4"><circle cx="8" cy="3" r="1.6"/><path d="M8 4.6V14M4.5 7h7M2.5 10a5.5 5 0 0 0 11 0"/></svg>
      <div class="eyebrow" style="margin-top:8px">On the water and beyond</div>
      <h2 class="display">OUR SERVICES</h2>
      <span class="btn btn-tan">View Our All Reviews <span class="ring">&#8595;</span></span>
    </div>
    <div class="svc-row">
      <div class="svc">
        <div class="ph" role="img" aria-label="Photograph of students training at the helm of a boat"></div>
        <div class="svc-ico"><svg width="26" height="20" viewBox="0 0 26 20" fill="none" stroke="currentColor" stroke-width="1.4"><path d="M2 13h22l-3 5H5zM7 13V7h10l3 6"/></svg></div>
        <h4>BOAT TRAINING</h4>
        <p>Hands-on instruction for new and experienced boaters.</p>
        <svg class="go" width="28" height="10" viewBox="0 0 28 10" fill="none" stroke="#fff"><path d="M0 5h26M22 1l4 4-4 4"/></svg>
      </div>
      <div class="svc svc-feature">
        <div class="ph" role="img" aria-label="Photograph of two guests smiling aboard a charter boat"></div>
        <h4>CHARTERS</h4>
        <p>Relax and explore<br>with captain-guided charters.</p>
        <div class="link">View charters</div>
        <svg class="go" width="28" height="10" viewBox="0 0 28 10" fill="none" stroke="#fff"><path d="M0 5h26M22 1l4 4-4 4"/></svg>
      </div>
      <div class="svc">
        <div class="ph" role="img" aria-label="Photograph of a motorboat under a bridge at sunset" style="background:linear-gradient(180deg,#e0a45a,#4a6480)"></div>
        <div class="svc-ico"><svg width="24" height="20" viewBox="0 0 24 20" fill="none" stroke="currentColor" stroke-width="1.4"><path d="M2 3h8c1 0 2 1 2 2v13c0-1-1-2-2-2H2zM22 3h-8c-1 0-2 1-2 2v13c0-1 1-2 2-2h8z"/></svg></div>
        <h4>FIRST MATE SERIES</h4>
        <p>Books to help you make informed decisions on and off the water.</p>
        <svg class="go" width="28" height="10" viewBox="0 0 28 10" fill="none" stroke="#fff"><path d="M0 5h26M22 1l4 4-4 4"/></svg>
      </div>
      <div class="svc">
        <div class="ph" role="img" aria-label="Photograph of a captain coaching a student while driving a boat"></div>
        <div class="svc-ico"><svg width="24" height="22" viewBox="0 0 24 22" fill="none" stroke="currentColor" stroke-width="1.4"><circle cx="12" cy="6" r="3"/><circle cx="5" cy="9" r="2.3"/><circle cx="19" cy="9" r="2.3"/><path d="M6 20c0-4 3-7 6-7s6 3 6 7"/></svg></div>
        <h4>PRIVATE COACHING</h4>
        <p>Personalized training for your goals.</p>
        <svg class="go" width="28" height="10" viewBox="0 0 28 10" fill="none" stroke="#fff"><path d="M0 5h26M22 1l4 4-4 4"/></svg>
      </div>
    </div>
  </div>
</section>

<section class="contact">
  <div class="contact-form">
    <h2 class="display">LEAVE A NOTE AND<br>I'LL GET BACK TO YOU!</h2>
    <div class="fields">
      <div class="field">First name</div><div class="field">Last name</div>
      <div class="field">Email Id</div><div class="field">Phone Number</div>
      <div class="field wide">Write a message</div>
    </div>
    <div class="submit">Submit Now</div>
  </div>
  <div class="contact-photo" role="img" aria-label="Photograph of a father with two daughters in life jackets on a boat"></div>
</section>

<footer class="site-footer">
  <div class="foot-brand">
    <div class="brand-mark"></div>
    <h5>Captain Harlan's Boat Training &amp; Charters, LLC</h5>
    <p>Hands-on boat training and charter services throughout the Gulf Bay area.</p>
  </div>
  <div class="foot-divider"></div>
  <div class="foot-col" style="left:489px"><h6>Quick Links</h6><ul><li>Home</li><li>Services</li><li>Boating Aids</li><li>Gallery</li><li>Contact</li></ul></div>
  <div class="foot-col" style="left:635px"><h6>Contact Us</h6><ul>
    <li><svg width="10" height="13" viewBox="0 0 10 13" fill="#222"><path d="M5 0a5 5 0 0 0-5 5c0 4 5 8 5 8s5-4 5-8a5 5 0 0 0-5-5zm0 7a2 2 0 1 1 0-4 2 2 0 0 1 0 4z"/></svg>Bayport, Florida</li>
    <li><svg width="11" height="11" viewBox="0 0 12 12" fill="#222"><path d="M2 0l2 3-1 1.5c.8 1.8 2 3 3.5 3.5L8 7l3 2-1 2.5C5 11.5.5 7 .5 1.5z"/></svg>(555) 014-2290</li>
    <li><svg width="12" height="9" viewBox="0 0 12 9" fill="none" stroke="#222"><rect x=".5" y=".5" width="11" height="8"/><path d="M.5.5l5.5 4 5.5-4"/></svg><span class="mail">hello@trelvanox482.com</span></li>
  </ul></div>
  <div class="foot-col" style="left:849px"><h6>Our Books</h6><ul><li>First Mate Buy</li><li>First Mate Trip</li><li>First Mate Throttle</li></ul></div>
  <div class="foot-col" style="left:1035px"><h6>Social Links</h6><ul><li>Friendwall</li><li>Snapgrid</li><li>Chirpline</li><li>Workring</li></ul></div>
</footer>
<div class="copyright">©2026 by Captain Harlan's Boat Training &amp; Charters, LLC</div>

</body>
</html>
```